Book Flyer

I want a flyer that we can use to promote this book to educators and to leaders....below is a sample flyer but I want something bold and creative and different from this....it can be completely different from what is attached. I want to be a WOW to increase sales. Please include pic of book and how folks can get a copy....I've given you a few pics but please be creative ....looking for a wow.

```html
<!DOCTYPE html>
<html lang="en">
<head>
<meta charset="utf-8">
<title>Intentional Excellence – Book Flyer</title>
<link rel="stylesheet" href="https://fonts.googleapis.com/css2?family=Oswald:wght@500;600&family=Roboto:wght@300;400;500&display=swap">
<style>
  :root {
    --ink: #151515;
    --charcoal: #2b2b2b;
    --gold: #f5a623;
    --red: #d4494a;
    --blue: #1e63b0;
    --blue-deep: #123f78;
    --white: #ffffff;
    --text: #2a2a2a;
  }
  * { box-sizing: border-box; margin: 0; padding: 0; }
  html, body { width: 990px; height: 1200px; overflow: hidden; background: var(--white); }
  .flyer { position: relative; width: 990px; height: 1200px; font-family: "Roboto", sans-serif; overflow: hidden; }

  .hero { position: absolute; left: 0; top: 0; width: 990px; height: 520px;
    background: radial-gradient(ellipse at 60% 70%, #4a4a4a 0%, var(--charcoal) 45%, var(--ink) 100%); }
  .portrait { position: absolute; left: 12px; top: 14px; width: 460px; height: 430px;
    background: linear-gradient(180deg, #6a5a52 0%, #cdd3e2 45%, #b9c2d6 100%); border-radius: 200px 200px 0 0; }

  .title { position: absolute; left: 494px; top: 86px; width: 472px; font-family: "Oswald", sans-serif; font-weight: 600;
    font-size: 46px; letter-spacing: -0.5px; color: var(--white); line-height: 1; white-space: nowrap; }
  .title span { color: var(--gold); }
  .title-rule { position: absolute; left: 496px; top: 169px; width: 245px; height: 2px; background: var(--gold); }
  .about-heading { position: absolute; left: 496px; top: 186px; font-weight: 300; font-size: 27px; color: var(--gold); }
  .about-text { position: absolute; left: 496px; top: 230px; width: 470px; font-weight: 300; font-size: 17px;
    line-height: 27.3px; color: var(--white); }

  .strategy-band { position: absolute; left: 0; top: 440px; width: 990px; height: 372px; }
  .strategy-heading { position: absolute; left: 26px; top: 468px; font-family: "Oswald", sans-serif; font-weight: 500;
    font-size: 23px; color: var(--white); letter-spacing: -0.3px; }

  .card { position: absolute; top: 548px; width: 272px; height: 202px; border: 2px solid var(--white);
    border-radius: 9px; color: var(--white); padding: 20px 16px 0; }
  .card-title { display: flex; justify-content: center; align-items: center; gap: 8px; font-family: "Oswald", sans-serif;
    font-weight: 500; font-size: 23px; margin-bottom: 14px; }
  .card-quote { font-size: 17px; font-weight: 300; line-height: 20.5px; text-align: justify; }
  .card-quote + .card-quote { margin-top: 10px; }
  .card-author { position: absolute; left: 20px; bottom: -17px; width: 228px; height: 34px; background: var(--red);
    border: 2px solid var(--white); border-radius: 17px; text-align: center; font-size: 17px; line-height: 30px; }

  .review { position: absolute; left: 26px; top: 872px; width: 668px; font-size: 17px; line-height: 26px;
    color: var(--text); text-align: justify; }
  .review-mark { color: var(--blue); font-family: "Oswald", sans-serif; font-size: 54px; line-height: 0; vertical-align: -20px;
    margin-right: 8px; }
  .review-author { position: absolute; left: 26px; top: 1030px; font-size: 17px; color: var(--text); }

  .book { position: absolute; left: 724px; top: 792px; width: 222px; height: 376px; transform: rotate(3deg);
    background: linear-gradient(180deg, #16294e 0%, #1d3d72 40%, var(--red) 48%, var(--red) 62%, #f3f3f3 63%, #e6e6e6 100%);
    box-shadow: 6px 8px 14px rgba(0,0,0,.35); }

  .footer { position: absolute; left: 0; top: 1090px; width: 990px; height: 110px; }
  .email { position: absolute; left: 306px; top: 1086px; width: 372px; height: 42px; background: var(--red); border-radius: 14px;
    border: 2px solid var(--white); color: var(--white); font-weight: 500; font-size: 17px; text-align: center; line-height: 38px; }
  .website { position: absolute; left: 0; width: 990px; top: 1150px; text-align: center; color: var(--white);
    font-weight: 500; font-size: 17px; letter-spacing: 4px; }
  .social { position: absolute; left: 32px; top: 1148px; display: flex; align-items: center; gap: 8px;
    color: var(--white); font-size: 15px; font-weight: 400; }
  .social-dot { width: 26px; height: 26px; border: 2px solid var(--white); border-radius: 50%; }
</style>
</head>
<body>
<main class="flyer">

  <section class="hero">
    <div class="portrait" role="img" aria-label="Portrait photo of the author in a shirt and tie"></div>
    <h1 class="title">INTENTIONAL <span>EXCELLENCE</span></h1>
    <div class="title-rule"></div>
    <h2 class="about-heading">ABOUT DR. HALE</h2>
    <p class="about-text">Distinguished as a vibrant, visionary, and innovative leader who recognizes that humility is the most important trait a leader can possess. Dr. Hale uses his prior experiences in business, education and nonprofit to assist organization leaders from all industries build internal leadership capacity, including strategic &amp; talent management and development to maximize organizational potential and success.</p>
  </section>

  <svg class="strategy-band" viewBox="0 0 990 372" aria-hidden="true">
    <polygon points="0,0 495,0 605,78 990,78 990,372 510,372 494,360 478,372 0,372" fill="#d4494a"/>
  </svg>
  <h3 class="strategy-heading">3 FUNDAMENTAL STRATEGIES THAT DRIVE LEADERSHIP</h3>

  <article class="card" style="left:51px">
    <div class="card-title">
      <svg width="30" height="26" viewBox="0 0 30 26" aria-hidden="true"><g fill="none" stroke="#fff" stroke-width="2"><line x1="15" y1="2" x2="15" y2="23"/><line x1="4" y1="6" x2="26" y2="6"/><line x1="8" y1="24" x2="22" y2="24"/><path d="M4 6 L0 15 H8 Z"/><path d="M26 6 L22 15 H30 Z"/></g></svg>
      EQUITY
    </div>
    <p class="card-quote">‘Fairness does not mean everyone gets the same.</p>
    <p class="card-quote">Fairness means everyone gets what they need.’</p>
    <div class="card-author">-Owen Fairley</div>
  </article>

  <article class="card" style="left:358px">
    <div class="card-title">
      <svg width="24" height="28" viewBox="0 0 24 28" aria-hidden="true"><path d="M12 2a8 8 0 0 1 8 8c0 6-8 13-8 13S4 16 4 10a8 8 0 0 1 8-8z" fill="none" stroke="#fff" stroke-width="2.4"/><circle cx="12" cy="10" r="3" fill="#fff"/><ellipse cx="12" cy="25" rx="10" ry="2" fill="none" stroke="#fff" stroke-width="1.6"/></svg>
      CHANGE
    </div>
    <p class="card-quote">‘If you do not change direction, you may end up where you are heading.’</p>
    <div class="card-author">-Chen Wu Lan</div>
  </article>

  <article class="card" style="left:664px">
    <div class="card-title">
      <svg width="30" height="24" viewBox="0 0 30 24" aria-hidden="true"><path d="M3 10c0-5 5-8 11-8s11 3 11 8-5 8-11 8c-2 0-3 0-5-1l-5 3 1-4c-1-2-2-4-2-6z" fill="#fff"/><circle cx="9" cy="10" r="1.6" fill="#d4494a"/><circle cx="14" cy="10" r="1.6" fill="#d4494a"/><circle cx="19" cy="10" r="1.6" fill="#d4494a"/></svg>
      COMMUNICATION
    </div>
    <p class="card-quote">‘The single biggest problem in communication is the illusion that is has taken place.’</p>
    <div class="card-author">-Edwin Marsh Cole</div>
  </article>

  <p class="review"><span class="review-mark">“</span>Intentional Excellence is a book written for all leaders. Dr. Marcus Hale speaks from real life experiences that are relatable and from the heart. His leadership steps have helped him develop into one of the most accomplished administrative leaders in the country. The three specific strategies outlined in this book will transform your leadership skills and help you stay on track to ensure success.</p>
  <p class="review-author">- Karen Whitfield, Principal</p>

  <svg class="footer" viewBox="0 0 990 110" aria-hidden="true">
    <defs>
      <linearGradient id="footerBlue" x1="0" y1="0" x2="1" y2="0">
        <stop offset="0" stop-color="#1e63b0"/><stop offset="1" stop-color="#123f78"/>
      </linearGradient>
    </defs>
    <path d="M0 22 Q495 -6 990 30 V110 H0 Z" fill="#c9d7ea"/>
    <path d="M0 30 Q495 2 990 40 V110 H0 Z" fill="url(#footerBlue)"/>
  </svg>

  <div class="book" role="img" aria-label="3D cover of the book Intentional Excellence with rising arrows artwork"></div>

  <div class="email">INFO@DRMARCUSHALE.COM</div>
  <div class="social"><span class="social-dot"></span>Hale Leadership</div>
  <div class="website">www.drmarcushale.com</div>

</main>
</body>
</html>
```